International industry company needs New Email Marketing Design

We need a new Email Marketing Design with the content in the attachment (html file).

Target Market(s)

engineers, technical directors, technologists, scientists from the aviation, defense, space and energy industries.

Font styles to use
Sans Serif

Requirements
Must have
• brio.vantel logo
photo of a gas turbine.
Should not have
• it cannot contain elements indicating material testing

```html
<!DOCTYPE html>
<html lang="en">
<head>
<meta charset="utf-8">
<title>brio.vantel – Machining of Specimens &amp; Test Samples</title>
<link rel="stylesheet" href="https://fonts.googleapis.com/css2?family=Saira+Semi+Condensed:wght@500;700&family=Roboto:wght@400;500;700&display=swap">
<style>
  :root {
    --navy: #27397a;
    --orange: #f07f1a;
    --orange-band: #f2a53a;
    --ink: #1c1c1c;
    --white: #ffffff;
    --footer: #1d1d1f;
    --hero-dark: #3a3a36;
    --hero-warm: #7a6a3a;
  }
  * { box-sizing: border-box; margin: 0; padding: 0; }
  html, body { width: 1200px; height: 4011px; overflow: hidden; }
  body { position: relative; background: var(--white); font-family: "Roboto", sans-serif; color: var(--ink); }
  .abs { position: absolute; }
  .display { font-family: "Saira Semi Condensed", sans-serif; font-weight: 700; }

  /* Hero */
  .hero { left: 0; top: 0; width: 1200px; height: 845px;
    background: radial-gradient(ellipse at 55% 55%, #8a8a84 0%, #5a5850 35%, var(--hero-dark) 75%),
                linear-gradient(180deg, var(--hero-warm), var(--hero-dark)); }
  .hero-shade { left: 0; top: 0; width: 1200px; height: 845px; background: rgba(20,20,20,0.35); }
  .brand { font-family: "Saira Semi Condensed", sans-serif; font-weight: 700; letter-spacing: 1px; }
  .hero .brand { left: 86px; top: 62px; font-size: 70px; line-height: 80px; color: var(--white); }
  .social { top: 66px; width: 74px; height: 74px; border-radius: 50%; background: rgba(255,255,255,0.85); }
  .hero-title { left: 0; width: 1200px; top: 370px; text-align: center; color: var(--white);
    font-size: 70px; line-height: 75px; }

  /* Intro */
  .greeting { left: 0; width: 1200px; top: 948px; text-align: center; color: var(--navy); font-size: 58px; line-height: 70px; }
  .intro { left: 70px; width: 1060px; top: 1040px; text-align: center; font-size: 26px; line-height: 39px; }
  .lead { left: 69px; top: 1260px; font-size: 26px; font-weight: 700; }
  .tests { left: 68px; top: 1338px; list-style: none; }
  .tests li { display: flex; align-items: center; height: 46.7px; font-family: "Saira Semi Condensed", sans-serif;
    font-weight: 500; font-size: 24px; color: var(--navy); }
  .tests svg { width: 25px; height: 25px; margin-right: 21px; flex: none; }
  .specimens-visual { left: 708px; top: 1424px; width: 366px; height: 428px;
    background: radial-gradient(ellipse at 60% 55%, #d8d8d8 0%, #f4f4f4 55%, #ffffff 80%); }
  .cta { left: 90px; top: 1920px; width: 1021px; height: 89px; border-radius: 10px; background: var(--navy);
    color: var(--white); font-family: "Saira Semi Condensed", sans-serif; font-weight: 700; font-size: 27px;
    display: flex; align-items: center; justify-content: center; }

  /* Accessories */
  .accessories { left: 0; top: 2150px; width: 1200px; height: 822px;
    background: radial-gradient(ellipse at 75% 60%, #f0a84a 0%, var(--orange-band) 45%, #e0902a 100%); }
  .acc-title { left: 0; width: 1200px; top: 2252px; text-align: center; color: var(--white); font-size: 58px; line-height: 70px; }
  .acc-sub { left: 0; width: 1200px; top: 2342px; text-align: center; color: var(--white); font-size: 26px; font-weight: 700; }
  .fixture-card { left: 166px; top: 2443px; width: 389px; height: 389px; border-radius: 30px; background: var(--white); }
  .fixture-visual { left: 226px; top: 2490px; width: 270px; height: 290px; border-radius: 8px;
    background: linear-gradient(160deg, #e6e6e6, #a8a8a8 60%, #d8d8d8); }
  .acc-list { left: 637px; list-style: none; color: var(--white);
    font-family: "Saira Semi Condensed", sans-serif; font-weight: 500; font-size: 24px; line-height: 34px; }
  .acc-list li { display: flex; align-items: flex-start; }
  .acc-list svg { width: 25px; height: 25px; margin: 5px 21px 0 0; flex: none; }

  /* Contact */
  .contact-title { left: 0; width: 1200px; top: 3075px; text-align: center; color: var(--navy); font-size: 58px; line-height: 64px; }
  .company { left: 0; width: 1200px; top: 3244px; text-align: center; font-size: 26px; line-height: 36px; font-weight: 500; }
  .divider { left: 553px; top: 3345px; width: 100px; height: 3px; background: var(--orange); }
  .contact-icon { width: 60px; height: 60px; }
  .contact-text { font-size: 26px; line-height: 40px; }

  /* Footer */
  .footer { left: 0; top: 3741px; width: 1200px; height: 270px; background: var(--footer); }
  .footer .brand { left: 0; width: 1200px; top: 3808px; text-align: center; font-size: 58px; line-height: 70px; color: #3b5bb5; }
  .copyright { left: 0; width: 1200px; top: 3898px; text-align: center; color: var(--white); font-size: 26px; }
</style>
</head>
<body>

<!-- Hero -->
<div class="abs hero" role="img" aria-label="Photo of a large gas turbine rotor in an industrial workshop"></div>
<div class="abs hero-shade"></div>
<div class="abs brand">
</div>
<header>
  <div class="abs brand" style="left:86px;top:62px;font-size:70px;line-height:80px;color:#fff;">brio.vantel</div>
  <div class="abs social" style="left:935px;" aria-label="Professional network profile"></div>
  <div class="abs social" style="left:1024px;" aria-label="Video channel"></div>
  <h1 class="abs hero-title display">Machining of Specimens<br>&amp; Test Samples</h1>
</header>

<!-- Intro -->
<h2 class="abs greeting display">Dear Surface Coating Circle Members,</h2>
<p class="abs intro">Corvalith manufactures high quality test coupons, specimens, samples, buttons, panels, discs, and strips for Thermal and Cold Spray facilities mainly in the aviation industry. We specialize in cutting difficult-to-machine aerospace grade materials such as nickel &amp; cobalt base superalloys, titanium, and hardened steel.</p>
<p class="abs lead">Our experience includes manufacturing specimens used for:</p>

<ul class="abs tests">
  <li><svg viewBox="0 0 24 24"><circle cx="12" cy="12" r="12" fill="#f07f1a"/><path d="M6 12h10M12 7l5 5-5 5" stroke="#fff" stroke-width="2.6" fill="none" stroke-linecap="round" stroke-linejoin="round"/></svg>Adhesion, cohesive and bond strength test of coating</li>
  <li><svg viewBox="0 0 24 24"><circle cx="12" cy="12" r="12" fill="#f07f1a"/><path d="M6 12h10M12 7l5 5-5 5" stroke="#fff" stroke-width="2.6" fill="none" stroke-linecap="round" stroke-linejoin="round"/></svg>Tensile test</li>
  <li><svg viewBox="0 0 24 24"><circle cx="12" cy="12" r="12" fill="#f07f1a"/><path d="M6 12h10M12 7l5 5-5 5" stroke="#fff" stroke-width="2.6" fill="none" stroke-linecap="round" stroke-linejoin="round"/></svg>Hardness test</li>
  <li><svg viewBox="0 0 24 24"><circle cx="12" cy="12" r="12" fill="#f07f1a"/><path d="M6 12h10M12 7l5 5-5 5" stroke="#fff" stroke-width="2.6" fill="none" stroke-linecap="round" stroke-linejoin="round"/></svg>Microstructure evaluation</li>
  <li><svg viewBox="0 0 24 24"><circle cx="12" cy="12" r="12" fill="#f07f1a"/><path d="M6 12h10M12 7l5 5-5 5" stroke="#fff" stroke-width="2.6" fill="none" stroke-linecap="round" stroke-linejoin="round"/></svg>Fatigue test</li>
  <li><svg viewBox="0 0 24 24"><circle cx="12" cy="12" r="12" fill="#f07f1a"/><path d="M6 12h10M12 7l5 5-5 5" stroke="#fff" stroke-width="2.6" fill="none" stroke-linecap="round" stroke-linejoin="round"/></svg>Lap shear test</li>
  <li><svg viewBox="0 0 24 24"><circle cx="12" cy="12" r="12" fill="#f07f1a"/><path d="M6 12h10M12 7l5 5-5 5" stroke="#fff" stroke-width="2.6" fill="none" stroke-linecap="round" stroke-linejoin="round"/></svg>Bend test</li>
  <li><svg viewBox="0 0 24 24"><circle cx="12" cy="12" r="12" fill="#f07f1a"/><path d="M6 12h10M12 7l5 5-5 5" stroke="#fff" stroke-width="2.6" fill="none" stroke-linecap="round" stroke-linejoin="round"/></svg>Erosion test</li>
  <li><svg viewBox="0 0 24 24"><circle cx="12" cy="12" r="12" fill="#f07f1a"/><path d="M6 12h10M12 7l5 5-5 5" stroke="#fff" stroke-width="2.6" fill="none" stroke-linecap="round" stroke-linejoin="round"/></svg>Stress corrosion test</li>
  <li><svg viewBox="0 0 24 24"><circle cx="12" cy="12" r="12" fill="#f07f1a"/><path d="M6 12h10M12 7l5 5-5 5" stroke="#fff" stroke-width="2.6" fill="none" stroke-linecap="round" stroke-linejoin="round"/></svg>Hoffman Scratch test</li>
  <li><svg viewBox="0 0 24 24"><circle cx="12" cy="12" r="12" fill="#f07f1a"/><path d="M6 12h10M12 7l5 5-5 5" stroke="#fff" stroke-width="2.6" fill="none" stroke-linecap="round" stroke-linejoin="round"/></svg>The cyclic furnace oxidation test (FCT)</li>
</ul>
<div class="abs specimens-visual" role="img" aria-label="Machined metal specimens: threaded round bar, flat strip, disc and small plate"></div>

<div class="abs cta">Read more about our made test coupons and specimens here!</div>

<!-- Custom laboratory accessories -->
<section>
  <div class="abs accessories" role="img" aria-label="Orange-tinted photo of a gas turbine rotor in a workshop"></div>
  <h2 class="abs acc-title display">Custom Laboratory Accessories</h2>
  <p class="abs acc-sub">Machining of laboratory related tools:</p>
  <div class="abs fixture-card"></div>
  <div class="abs fixture-visual" role="img" aria-label="Steel V-grooved curing fixture"></div>
  <ul class="abs acc-list" style="top:2512px;">
    <li><svg viewBox="0 0 24 24"><circle cx="12" cy="12" r="12" fill="#fff"/><path d="M6 12h10M12 7l5 5-5 5" stroke="#f2a53a" stroke-width="2.6" fill="none" stroke-linecap="round" stroke-linejoin="round"/></svg>Gravity or pressure type V-grooved<br>curing fixture for Tensile Bond<br>Strength test of coating</li>
  </ul>
  <ul class="abs acc-list" style="top:2648px;">
    <li style="margin-bottom:13px;"><svg viewBox="0 0 24 24"><circle cx="12" cy="12" r="12" fill="#fff"/><path d="M6 12h10M12 7l5 5-5 5" stroke="#f2a53a" stroke-width="2.6" fill="none" stroke-linecap="round" stroke-linejoin="round"/></svg>Loading fixture</li>
    <li><svg viewBox="0 0 24 24"><circle cx="12" cy="12" r="12" fill="#fff"/><path d="M6 12h10M12 7l5 5-5 5" stroke="#f2a53a" stroke-width="2.6" fill="none" stroke-linecap="round" stroke-linejoin="round"/></svg>and more...</li>
  </ul>
</section>

<!-- Contact -->
<section>
  <h2 class="abs contact-title display">Do not hesitate to contact us,<br>if you have any questions.</h2>
  <p class="abs company">Corvalith Sp. z o.o.<br>Science and Technology Park 'Halvern'</p>
  <div class="abs divider"></div>

  <svg class="abs contact-icon" style="left:233px;top:3430px;" viewBox="0 0 60 60" aria-hidden="true">
    <circle cx="30" cy="30" r="28" fill="none" stroke="#f07f1a" stroke-width="3"/>
    <path d="M30 18c-5 0-8.5 3.6-8.5 8.3 0 6 8.5 15.7 8.5 15.7s8.5-9.7 8.5-15.7C38.5 21.6 35 18 30 18z" fill="#27397a"/>
    <circle cx="30" cy="26.5" r="3.2" fill="#fff"/>
  </svg>
  <p class="abs contact-text" style="left:321px;top:3418px;">Marlow Lane 12 bud. 4C street<br>07-210 Brenvik, Poland</p>

  <svg class="abs contact-icon" style="left:233px;top:3547px;" viewBox="0 0 60 60" aria-hidden="true">
    <circle cx="30" cy="30" r="28" fill="none" stroke="#f07f1a" stroke-width="3"/>
    <path d="M22 19c1.5-1 3-.8 3.8.6l2.2 4c.6 1.1.3 2.3-.6 3.1l-1.6 1.3c1.2 2.6 3.5 4.9 6 6.1l1.4-1.6c.8-.9 2-1.1 3.1-.5l4 2.2c1.4.8 1.6 2.3.6 3.8-1.6 2.4-4 3.6-6.7 2.8-7.4-2.2-13-7.8-15.2-15.2-.8-2.7.5-5.1 3-6.6z" fill="#27397a"/>
  </svg>
  <p class="abs contact-text" style="left:321px;top:3540px;">Phone:<br>+48 500 123 456</p>

  <svg class="abs contact-icon" style="left:624px;top:3547px;" viewBox="0 0 60 60" aria-hidden="true">
    <circle cx="30" cy="30" r="28" fill="none" stroke="#f07f1a" stroke-width="3"/>
    <rect x="19" y="22" width="22" height="16" rx="2" fill="none" stroke="#27397a" stroke-width="2.4"/>
    <path d="M19.5 23l10.5 8 10.5-8" fill="none" stroke="#27397a" stroke-width="2.4"/>
  </svg>
  <p class="abs contact-text" style="left:716px;top:3540px;">E - Mail :<br>info@corvalith.com</p>
</section>

<!-- Footer -->
<footer>
  <div class="abs footer"></div>
  <div class="abs brand">brio.vantel</div>
  <p class="abs copyright">Copyright © 2020 Brio Vantel, All rights reserved.</p>
</footer>

</body>
</html>
```